Popular Australian based wellbeing and high performance podcast needs a design

I need a new, fresh design for my Keep Rising Bright podcast image. This podcast helps and enables its listeners to do their life even better by enhancing their wellbeing, mindset, happiness and leadership. I would love to see designs that include the colour blue. The final design should communicate optimism, hope, approachability and credibility.

Target Market(s)

Target is teenagers to adults wanting to enhance their wellbeing, mindset and happiness.

Font styles to use
Other font styles liked:
• Proba Pro

Colors
33a6d7
0592cd
ffffff

Requirements
Must have
• Must include: Keep Rising Bright podcast
Nice to have
• Could include: with Miles Tervick.

```html
<!DOCTYPE html>
<html lang="en">
<head>
<meta charset="utf-8">
<title>Keep Rising Bright podcast – cover</title>
<link rel="stylesheet" href="https://fonts.googleapis.com/css2?family=Jost:wght@300;400;700&display=swap">
<style>
  :root {
    --page-bg: #f3f3f3;
    --frame-orange: #fbb11c;
    --sky-blue: #33a6d7;
    --deep-blue: #0592cd;
    --title-blue: #0aa2d9;
    --white: #ffffff;
  }
  * { margin: 0; padding: 0; box-sizing: border-box; }
  html, body {
    width: 1200px; height: 1200px; overflow: hidden;
    background: var(--page-bg);
    font-family: "Jost", "Century Gothic", sans-serif;
  }
  .cover {
    position: absolute; left: 214px; top: 214px;
    width: 773px; height: 773px;
    background: var(--frame-orange);
  }
  .cover__field {
    position: absolute; left: 11px; top: 11px; right: 11px; bottom: 11px;
    overflow: hidden;
    background: linear-gradient(180deg, var(--sky-blue) 0%, var(--deep-blue) 100%);
  }
  .cover__halo {
    position: absolute; left: 15px; top: -245px;
    width: 720px; height: 720px; border-radius: 50%;
    background: var(--white);
  }
  .cover__title {
    position: absolute; left: 0; right: 0; top: 18px;
    text-align: center; font-weight: 700;
    letter-spacing: -2px; line-height: 84px; font-size: 74px;
  }
  .cover__title-line { display: block; color: var(--frame-orange); }
  .cover__title-line--podcast { color: var(--title-blue); font-size: 80px; }
  .cover__host-photo {
    position: absolute; left: 110px; top: 280px;
    width: 520px; height: 480px;
    border-radius: 200px 200px 0 0;
    background: linear-gradient(180deg, #6b4a32 0%, #c99a7c 30%, #8fbde6 60%, #5f9fdc 100%);
  }
  .host-tag {
    position: absolute; left: 697px; top: 857px;
    width: 290px; height: 95px;
    background: var(--white);
    color: var(--title-blue);
    padding: 14px 0 0 16px;
  }
  .host-tag__lead { display: block; font-size: 25px; font-weight: 400; line-height: 28px; }
  .host-tag__name { display: block; font-size: 38px; font-weight: 300; line-height: 44px; letter-spacing: 0.5px; }
</style>
</head>
<body>
  <div class="cover">
    <div class="cover__field">
      <div class="cover__halo"></div>
      <h1 class="cover__title">
        <span class="cover__title-line">Keep</span>
        <span class="cover__title-line">Rising Bright</span>
        <span class="cover__title-line cover__title-line--podcast">podcast</span>
      </h1>
      <div class="cover__host-photo" role="img" aria-label="Portrait photo of the host, a smiling man with curly hair in a light blue shirt"></div>
    </div>
  </div>
  <div class="host-tag">
    <span class="host-tag__lead">With</span>
    <span class="host-tag__name">Miles Tervick</span>
  </div>
</body>
</html>
```